wealth management firm, professional group, new model

we have a logo that works but we need a card, white background using our colors...clean look

our tag line if can be used in

The Path From Saver to Investor

```html
<!DOCTYPE html>
<html lang="en">
<head>
<meta charset="utf-8">
<title>Vestara Wealth Partners — Business Card</title>
<link href="https://fonts.googleapis.com/css2?family=Montserrat:wght@400;500&display=swap" rel="stylesheet">
<style>
  :root {
    --navy: #1d2b4f;
    --card: #ffffff;
    --backdrop: #e6e7ea;
    --shadow: rgba(20, 25, 40, 0.18);
  }
  * { box-sizing: border-box; margin: 0; padding: 0; }
  html, body {
    width: 1200px;
    height: 900px;
    overflow: hidden;
    background: var(--backdrop);
    font-family: "Montserrat", Arial, sans-serif;
    color: var(--navy);
  }
  .stage {
    position: relative;
    width: 1200px;
    height: 900px;
  }
  .card {
    position: absolute;
    top: 302px;
    width: 514px;
    height: 296px;
    background: var(--card);
    border-radius: 22px;
    box-shadow: 0 6px 18px var(--shadow);
  }
  .card--front { left: 72px; }
  .card--back { left: 615px; }

  /* Front */
  .front-brand {
    position: absolute;
    left: 0; right: 0;
    top: 135px;
    text-align: center;
  }
  .brand-name {
    font-weight: 400;
    font-size: 40px;
    line-height: 1;
    letter-spacing: 0.5em;
    margin-right: -0.5em;
  }
  .brand-descriptor {
    font-weight: 400;
    font-size: 15px;
    letter-spacing: 0.13em;
    margin-top: 20px;
  }
  .tagline {
    position: absolute;
    left: 0; right: 0;
    top: 252px;
    text-align: center;
    font-size: 11px;
    letter-spacing: 0.26em;
    text-transform: uppercase;
  }

  /* Back */
  .back-brand {
    position: absolute;
    right: 44px;
    top: 75px;
    text-align: center;
  }
  .back-brand .brand-name {
    font-size: 28px;
    letter-spacing: 0.42em;
    margin-right: -0.42em;
  }
  .back-brand .brand-descriptor {
    font-size: 11.5px;
    margin-top: 14px;
  }
  .holder {
    position: absolute;
    left: 47px;
    top: 150px;
  }
  .holder-name {
    font-size: 18px;
    font-weight: 400;
    letter-spacing: 0.02em;
    line-height: 1.1;
  }
  .holder-title {
    font-size: 11.5px;
    letter-spacing: 0.04em;
    margin-top: 3px;
  }
  .contact-list {
    position: absolute;
    left: 47px;
    top: 223px;
    list-style: none;
    font-size: 11.5px;
    line-height: 15px;
  }
  .contact-label {
    display: inline-block;
    width: 18px;
  }
  .address {
    position: absolute;
    right: 44px;
    top: 238px;
    text-align: right;
    font-style: normal;
    font-size: 11.5px;
    line-height: 15px;
  }
</style>
</head>
<body>
<main class="stage">
  <section class="card card--front" aria-label="Card front">
    <div class="front-brand">
      <div class="brand-name">VESTARA</div>
      <div class="brand-descriptor">WEALTH PARTNERS</div>
    </div>
    <p class="tagline">The Path From Saver to Investor</p>
  </section>

  <section class="card card--back" aria-label="Card back">
    <div class="back-brand">
      <div class="brand-name">VESTARA</div>
      <div class="brand-descriptor">WEALTH PARTNERS</div>
    </div>
    <div class="holder">
      <div class="holder-name">DANIEL MARLOWE</div>
      <div class="holder-title">MANAGING DIRECTOR</div>
    </div>
    <ul class="contact-list">
      <li><span class="contact-label">P</span>555 010 24 68</li>
      <li><span class="contact-label">E</span>info@vestarawealth.com</li>
      <li><span class="contact-label">W</span>www.vestarawealth.com</li>
    </ul>
    <address class="address">
      48 Harbor Lane<br>
      Rivertown, New York 10510
    </address>
  </section>
</main>
</body>
</html>
```